Digital Marketing Website Redesign, modern, fresh, dynamic

Hi there, we would like to freshen up our website and create a new dynamic look. We are a digital marketing agency who specialise in digital transformation in the form of creating websites for appointment bookings. Our clients are service businesses such as hairdressers, dentists and doctors who's patients need to book appointments with them.

Our company name is Plombek with the point being we can help increase your revenue curve by increasing your appointment bookings.

Our services include building the website, creating campaigns to drive traffic, increasing conversions and monitoring and reporting.

We are playing with a tagline of 'Step into your Digital Transformation' as we have a 5 step journey that customers can take with us getting them from zero to full appointment bookings.

Our current website is www.plomnbek-site.example

You can see a draft design that I mocked up on Canva here https://www.drawpadhub.example/design/QXT82LmnB7K/PoWz41kdRtGyvb_sxE_JNq/edit?utm_content=QXT82LmnB7K&utm_campaign=designshare&utm_medium=link2&utm_source=sharebutton

Also attached some other homepage ideas. In regard to photos we are open to ideas.

Please let if you need any more information to provide us with an initial design. Thanks million and I look forward to receiving fantastic designs :)

Marissa Tobler
Plombek

Target Market(s)

Appointment based businesses such as hairdressers, dentists, doctors

Industry/Entity Type

Marketing and Digital

Coding

Coded - Design and coding required

Number of Pages Required

1 page

Colors
0094D4
00A9DD
6FCCEA
C7EBF8
E9F6FB

Requirements
Must have
• Appointment booking CTA
Nice to have
• A website we like https://www.morwenhalbrook.example

```html
<!DOCTYPE html>
<html lang="en">
<head>
<meta charset="utf-8">
<title>Plombek – Step into your Digital Transformation</title>
<link href="https://fonts.googleapis.com/css2?family=Lexend:wght@300;400;500;600;700&family=Open+Sans:ital,wght@0,400;0,500;0,600;1,400&display=swap" rel="stylesheet">
<style>
:root{
  --blue:#1b63b6;
  --blue-dark:#154f93;
  --sky:#0094d4;
  --sky-2:#6fccea;
  --sky-3:#c7ebf8;
  --sky-4:#e9f6fb;
  --purple:#6a0fe8;
  --ink:#1f2329;
  --text:#3a3f46;
  --muted:#9aa0a8;
  --page:#f5f6f8;
  --white:#ffffff;
}
*{margin:0;padding:0;box-sizing:border-box}
html,body{width:1200px;height:4234px;overflow:hidden}
body{background:var(--page);font-family:'Lexend',sans-serif;color:var(--ink);position:relative}
.abs{position:absolute}
a{color:inherit;text-decoration:none}

/* header */
.brand{left:82px;top:48px;font-size:30px;font-weight:600;color:var(--blue);letter-spacing:-.5px;display:flex;align-items:center;gap:10px}
.brand .dot{width:12px;height:12px;border-radius:50%;background:var(--sky)}
.nav{left:676px;top:52px;display:flex;gap:35px;font-size:16px;color:var(--ink)}

/* hero */
.hero-title{left:66px;top:214px;font-size:49px;font-weight:600;line-height:75px;color:#1d2229;letter-spacing:-1.2px;white-space:nowrap}
.hero-text{left:66px;top:370px;width:545px;font-size:19px;line-height:29px;color:var(--text);font-weight:300;letter-spacing:-.2px}
.btn{display:flex;align-items:center;justify-content:center;background:var(--blue);color:#fff;font-weight:500;border-radius:3px}
.hero-cta{left:66px;top:515px;width:153px;height:52px;font-size:16px}
.hero-more{left:254px;top:530px;font-size:16px;color:#6b7078}
.hero-art{left:636px;top:148px;width:490px;height:473px;border-radius:48% 52% 50% 50%/46% 50% 50% 54%;background:radial-gradient(circle at 55% 55%,#cfe3f3 0%,#e4edf4 55%,#eef1f4 100%)}

/* about */
.about-art{left:107px;top:756px;width:468px;height:436px;border-radius:50%;background:radial-gradient(circle at 50% 50%,#8fc3e8 0%,#b8daf1 50%,rgba(233,246,251,0) 75%)}
.eyebrow{font-size:16px;font-weight:500;color:var(--blue)}
.about-eyebrow{left:653px;top:838px}
.about-title{left:653px;top:864px;font-size:29px;font-weight:500}
.about-text{left:653px;top:920px;width:460px;font-size:17px;line-height:25.5px;color:var(--text);font-weight:300}
.about-btn{left:653px;top:1064px;width:118px;height:43px;font-size:12px}

/* products */
.products{left:0;top:1299px;width:1200px;height:624px;background:linear-gradient(180deg,#dce9f2,#e6eff5)}
.center{left:0;width:1200px;text-align:center}
.prod-eyebrow{top:1336px}
.prod-title{top:1360px;font-size:30px;font-weight:500;line-height:42px}
.plan{top:1493px;width:358px;height:397px;background:#fff;border-radius:6px;box-shadow:0 3px 12px rgba(30,60,100,.08);text-align:center;font-family:'Open Sans',sans-serif}
.plan h3{margin-top:22px;font-size:28px;font-weight:500;color:#111}
.plan .desc{margin:10px auto 0;width:310px;font-size:16px;font-style:italic;line-height:23px;color:#555}
.plan .old{margin-top:20px;font-size:15px;color:#999}
.plan .old s{margin-right:8px}
.plan .save{background:#dbeafb;color:var(--blue);font-weight:600;padding:2px 8px;border-radius:10px;font-size:15px}
.plan .from{margin-top:8px;font-size:16px;color:#777}
.plan .price{font-size:46px;font-weight:600;color:var(--blue);line-height:50px}
.plan .price small{font-size:20px}
.plan .free{margin-top:14px;font-size:16px;color:var(--blue);font-weight:500}
.plan .plan-btn{margin:14px auto 0;width:288px;height:46px;font-size:21px;font-weight:400;border-radius:2px}
.plan .more{margin-top:12px;font-size:16px;color:#aaa}
.plan.ultimate h3,.plan.ultimate .price,.plan.ultimate .free{color:var(--purple)}
.plan.ultimate .plan-btn{background:var(--purple)}
.badge{left:915px;top:1476px;width:140px;height:33px;background:var(--purple);color:#fff;border-radius:7px;font-family:'Open Sans',sans-serif;font-size:21px;display:flex;align-items:center;justify-content:center}

/* team */
.team-eyebrow{top:2010px}
.team-title{top:2033px;font-size:29px;font-weight:500;line-height:42px}
.member{top:2149px;width:171px;text-align:center}
.member .photo{width:171px;height:222px;background:linear-gradient(180deg,#7b7e82,#3a3d42)}
.member .name{margin-top:10px;font-size:16px}
.member .role{margin-top:4px;font-size:11px;color:var(--blue)}
.circle-btn{width:42px;height:42px;border:1.5px solid #333;border-radius:50%;display:flex;align-items:center;justify-content:center}
.dots{display:flex;gap:6px;align-items:center}
.dots i{display:block;width:6px;height:6px;border-radius:3px;background:#333}
.dots i.on{width:26px;background:var(--blue)}

/* testimonials */
.test-eyebrow{top:2580px}
.test-title{top:2604px;font-size:30px;font-weight:500}
.quote{width:255px;height:166px;background:#fff;border-radius:4px;box-shadow:0 2px 8px rgba(0,0,0,.05);padding:16px 16px 0 16px;font-size:10.5px;color:#666;line-height:15px;font-weight:300}
.quote .rm{color:var(--blue);font-weight:500;margin-top:4px;display:block}
.quote .who{position:absolute;left:16px;bottom:34px;font-size:15px;color:var(--ink);font-weight:400}
.quote .stars{position:absolute;left:16px;bottom:12px;color:var(--blue);font-size:16px;letter-spacing:2px}
.quote .when{position:absolute;right:16px;bottom:14px;font-size:10px;color:#888}

/* blog */
.blog-eyebrow{top:3172px}
.blog-title{top:3196px;font-size:30px;font-weight:500}
.post{top:3272px;width:296px;height:411px;background:#fff;padding:14px}
.post .img{width:268px;height:208px;border-radius:6px;position:relative}
.post .tag{position:absolute;right:20px;top:16px;color:#fff;font-size:13px}
.post h4{margin-top:20px;font-size:16.5px;font-weight:600;line-height:25px}
.post .date{margin-top:4px;font-size:12px;color:#bbb}
.post p{margin-top:8px;font-size:10.5px;line-height:16.5px;color:#666;font-weight:300}
.post .read{margin-top:8px;font-size:11px;color:var(--blue)}

/* cta */
.cta{left:0;top:3768px;width:1200px;height:145px;background:var(--sky-4)}
.cta-text{left:56px;top:3799px;font-size:30px;line-height:41px;color:var(--blue);font-weight:400}
.cta-text b{font-weight:600}
.cta-btn{left:907px;top:3817px;width:237px;height:48px;font-size:16px;border-radius:4px}

/* footer */
.f-brand{left:120px;top:3984px;font-size:38px;font-weight:600;color:var(--blue);display:flex;align-items:center;gap:10px}
.f-brand .dot{width:14px;height:14px;border-radius:50%;background:var(--sky)}
.f-addr{left:118px;top:4052px;width:260px;font-size:16.5px;line-height:23px;color:#222;font-weight:300}
.f-col h5{font-size:15px;font-weight:500;margin-bottom:12px}
.f-col div{font-size:10.5px;line-height:21px;color:#333;font-weight:300}
.f-col b{font-weight:500}
.social{left:934px;top:4131px;display:flex;gap:18px}
.social span{width:22px;height:22px;border-radius:50%;background:#b9bec5;display:block}
.f-line{left:115px;top:4171px;width:965px;height:1px;background:#9aa0a8}
.copy{top:4196px;font-size:10.5px;color:#777}
.code{left:1055px;top:4196px;font-size:10.5px;color:#777}
</style>
</head>
<body>

<header>
  <div class="abs brand"><span>Plombek</span><span class="dot"></span></div>
  <nav class="abs nav"><a>Home</a><a>Services</a><a>Testimonials</a><a>Blog</a><a>Contact</a></nav>
</header>

<section class="hero">
  <h1 class="abs hero-title">Step into your Digital<br>Transformation</h1>
  <p class="abs hero-text">Digital transformation is a journey. At Plombek we divide the journey into five key steps that take your business from comprehensive market research to full appointment bookings. Ready to go on that journey?</p>
  <a class="abs btn hero-cta">Get Started</a>
  <a class="abs hero-more">View More</a>
  <div class="abs hero-art" role="img" aria-label="Illustration of a person walking along a blue arrow path toward a digital transformation sign and a chip"></div>
</section>

<section class="about">
  <div class="abs about-art" role="img" aria-label="Illustration of a person beside a large monitor showing a world map with a search magnifier, star rating and chart icons"></div>
  <div class="abs eyebrow about-eyebrow">About Us</div>
  <h2 class="abs about-title">Your Reliable Digital Partner</h2>
  <p class="abs about-text">Lorem ipsum dolor sit amet consectetur. Laoreet at tristique nibh eget ullamcorper quis pulvinar. Urna pretium amet at semper ipsum. Pulvinar lectus est neque aliquam vitae. Sed non placerat dolor scelerisque venenatis ultrices tempus est viverra. Nisi.</p>
  <a class="abs btn about-btn">Learn More</a>
</section>

<section>
  <div class="abs products"></div>
  <div class="abs center eyebrow prod-eyebrow">Our Products</div>
  <h2 class="abs center prod-title">many steps you want to take on your<br>digital transformation journey</h2>

  <div class="abs plan" style="left:35px">
    <h3>Starter Plan</h3>
    <p class="desc">Online readiness review based on our 12 point checklist and Implementation</p>
    <div class="old"><s>€500.00</s><span class="save">SAVE 20%</span></div>
    <div class="from">Start From</div>
    <div class="price"><small>€</small>399.00</div>
    <div class="free">Free Consultation for FIRST TRIAL</div>
    <a class="btn plan-btn">Just take 2 Step Journey</a>
    <div class="more">View More</div>
  </div>
  <div class="abs plan" style="left:421px">
    <h3>Premium Plan</h3>
    <p class="desc">Online readiness review based on our 12 point checklist, Implementation and 3.</p>
    <div class="old"><s>€750.00</s><span class="save">SAVE 20%</span></div>
    <div class="from">Start From</div>
    <div class="price"><small>€</small>599.00</div>
    <div class="free">Free Consultation for FIRST TRIAL</div>
    <a class="btn plan-btn">Just take 3 Step Journey</a>
    <div class="more">View More</div>
  </div>
  <div class="abs plan ultimate" style="left:806px">
    <h3>Ultimate Plan</h3>
    <p class="desc">Online readiness review based on our 12 point checklist, Implementation and etc.</p>
    <div class="old"><s>€1200.00</s><span class="save">SAVE 25%</span></div>
    <div class="from">Start From</div>
    <div class="price"><small>€</small>899.00</div>
    <div class="free">Free Consultation for FIRST TRIAL</div>
    <a class="btn plan-btn">Take All the Full Journey</a>
    <div class="more">View More</div>
  </div>
  <div class="abs badge">Best Seller</div>
</section>

<section>
  <div class="abs center eyebrow team-eyebrow">Our Teams</div>
  <h2 class="abs center team-title">Our Team Has All The Experience<br>Your Business Needs</h2>
  <div class="abs member" style="left:90px"><div class="photo" role="img" aria-label="Portrait photo of Corwin in a dark suit"></div><div class="name">Corwin</div><div class="role">Account Manager</div></div>
  <div class="abs member" style="left:302px"><div class="photo" role="img" aria-label="Portrait photo of Liesel in a dark blazer"></div><div class="name">Liesel</div><div class="role">Website Specialist</div></div>
  <div class="abs member" style="left:515px"><div class="photo" role="img" aria-label="Portrait photo of Bramwell in a dark suit"></div><div class="name">Bramwell</div><div class="role">Account Manager</div></div>
  <div class="abs member" style="left:727px"><div class="photo" role="img" aria-label="Portrait photo of Odette in a grey jacket"></div><div class="name">Odette</div><div class="role">Content Creator</div></div>
  <div class="abs member" style="left:939px"><div class="photo" role="img" aria-label="Portrait photo of Varesh in a dark suit"></div><div class="name">Varesh</div><div class="role">Web Developer</div></div>

  <div class="abs circle-btn" style="left:515px;top:2452px"><svg width="22" height="12" viewBox="0 0 22 12"><path d="M21 6H2M7 1L2 6l5 5" fill="none" stroke="#333" stroke-width="1.5"/></svg></div>
  <div class="abs dots" style="left:574px;top:2470px"><i class="on"></i><i></i><i></i></div>
  <div class="abs circle-btn" style="left:643px;top:2452px"><svg width="22" height="12" viewBox="0 0 22 12"><path d="M1 6h19M15 1l5 5-5 5" fill="none" stroke="#333" stroke-width="1.5"/></svg></div>
</section>

<section>
  <div class="abs center eyebrow test-eyebrow">Testimonials</div>
  <h2 class="abs center test-title">What Our Client Say</h2>

  <div class="abs quote" style="left:-34px;top:2675px">Lorem ipsum dolor sit amet consectetur. Cursus nisi felis imperdiet diam risus gravida. Tortor arcu in purus blandit.<span class="rm">Read More</span><div class="stars">★★★★★</div><div class="when">4 days ago</div></div>
  <div class="abs quote" style="left:242px;top:2675px">Lorem ipsum dolor sit amet consectetur. Lectus facilisi consequat pellentesque amet volutpat est massa velit. Egestas condimentum quisque.<div class="who">Fernwick</div><div class="stars">★★★★★</div><div class="when">4 days ago</div></div>
  <div class="abs quote" style="left:518px;top:2675px">Lorem ipsum dolor sit amet consectetur. Et ultrices vehicula turpis porta dictum. Ac mollis diam auctor massa eget tincidunt non.<span class="rm">Read More</span><div class="who">Tom Arrowdale</div><div class="stars">★★★★★</div><div class="when">6 days ago</div></div>
  <div class="abs quote" style="left:794px;top:2675px">Lorem ipsum dolor sit amet consectetur. Sem condimentum non eu amet ullamcorper pellentesque auctor. Tincidunt odio at eu.<div class="who">Neil Brackett</div><div class="stars">★★★★★</div><div class="when">6 days ago</div></div>
  <div class="abs quote" style="left:1070px;top:2675px">Lorem ipsum dolor sit amet. Pretium metus amet rutrum egestas phasellus facilisi.<div class="who">Oren</div><div class="stars">★★★★★</div><div class="when">1 week ago</div></div>

  <div class="abs quote" style="left:-131px;top:2861px">Lorem ipsum amet consectetur. Sed nibh varius. Risus mattis erat dignissim mauris mollis nullam nisi. Diam.<div class="stars">★★★★★</div><div class="when">1 week ago</div></div>
  <div class="abs quote" style="left:145px;top:2861px">Lorem ipsum dolor sit amet consectetur. Ante facilisis mi luctus aenean sit sed egestas mi ac. At at ut pellentesque in maecenas diam. Vel pulvinar mattis id duis ante lacus porttitor.<div class="who">Pim</div><div class="stars">★★★★★</div><div class="when">November 27</div></div>
  <div class="abs quote" style="left:421px;top:2861px">Lorem ipsum dolor sit amet consectetur. Cras non eget nunc fames nec nulla mollis amet potenti. Nisl elit auctor dui lacus lorem magna nulla lacinia.<div class="who">Nadia Fairholm</div><div class="stars">★★★★★</div><div class="when">November 26</div></div>
  <div class="abs quote" style="left:697px;top:2861px">Lorem ipsum dolor sit amet consectetur. Phasellus nisl tincidunt consectetur massa cras. Pellentesque ut integer quis diam volutpat nibh.<span class="rm">Read More</span><div class="who">Rory Castellan</div><div class="stars">★★★★★</div><div class="when">November 22</div></div>
  <div class="abs quote" style="left:973px;top:2861px">Lorem ipsum dolor sit amet consectetur. Libero nulla nunc odio leo aenean et id pretium massa. Gravida mauris sit urna feugiat pretium tincidunt cursus.<span class="rm">Read More</span><div class="who">Desmond</div><div class="stars">★★★★★</div><div class="when">November 21</div></div>

  <div class="abs circle-btn" style="left:496px;top:3043px"><svg width="22" height="12" viewBox="0 0 22 12"><path d="M21 6H2M7 1L2 6l5 5" fill="none" stroke="#333" stroke-width="1.5"/></svg></div>
  <div class="abs dots" style="left:555px;top:3061px"><i class="on"></i><i></i><i></i><i></i><i></i><i></i></div>
  <div class="abs circle-btn" style="left:661px;top:3043px"><svg width="22" height="12" viewBox="0 0 22 12"><path d="M1 6h19M15 1l5 5-5 5" fill="none" stroke="#333" stroke-width="1.5"/></svg></div>
</section>

<section>
  <div class="abs center eyebrow blog-eyebrow">Blogs</div>
  <h2 class="abs center blog-title">Ahead Of The Curve</h2>

  <article class="abs post" style="left:99px">
    <div class="img" role="img" aria-label="Photo of a person relaxing on a sofa in a bright room" style="background:linear-gradient(160deg,#6e8b7a,#3f4a44)"><span class="tag">Special Events</span></div>
    <h4>5 Digital Tools For 2024</h4>
    <div class="date">22 July 2024</div>
    <p>Lorem ipsum dolor sit amet consectetur. Orci integer lectus sed orci pellentesque in faucibus ullamcorper. Non sed sed id viverra lectus sed orci pellentesque in faucibus lectus.</p>
    <div class="read">Read Full Post ⟶</div>
  </article>
  <article class="abs post" style="left:454px">
    <div class="img" role="img" aria-label="Photo of a laptop showing a marketing dashboard" style="background:linear-gradient(160deg,#c9d3dc,#6c7680)"><span class="tag">★ Special Events</span></div>
    <h4>5 Tips For Better Marketing This Year</h4>
    <div class="date">15 July 2024</div>
    <p>Lorem ipsum dolor sit amet consectetur. Euismod lacus cursus in bibendum molestie aenean at id consectetur. Lacus aliquam bibendum molestie aenean at id.</p>
    <div class="read">Read Full Post ⟶</div>
  </article>
  <article class="abs post" style="left:809px">
    <div class="img" role="img" aria-label="Photo of a person wearing a virtual reality headset in blue light" style="background:linear-gradient(160deg,#4b5bd6,#1d2258)"><span class="tag">★ Special Events</span></div>
    <h4>How To Use AI So It's Not Using You</h4>
    <div class="date">08 July 2024</div>
    <p>Are you in the dark when it comes to business taxes? We have got the lowdown on the key taxes your new business will need to pay, so you are on top of your tax liabilities.</p>
    <div class="read">Read Full Post ⟶</div>
  </article>
</section>

<section>
  <div class="abs cta"></div>
  <p class="abs cta-text"><b>Start your journey</b> by booking an appointment with us,<br>Book your free, no commitment appointment with us.</p>
  <a class="abs btn cta-btn">Book Your Appointment</a>
</section>

<footer>
  <div class="abs f-brand"><span>Plombek</span><span class="dot"></span></div>
  <p class="abs f-addr">Harbourgate Enterprise Hub Northfield Technical College, Brackenmoor, Co. Westmere, Lanover BK4 7QZ</p>
  <div class="abs f-col" style="left:445px;top:3963px"><h5>Company</h5><div>About Us<br>Services<br>Testimonials<br>Blog<br>Contact</div></div>
  <div class="abs f-col" style="left:620px;top:3963px"><h5>Opening Hours</h5><div>Mon - Fri: 08:30 am - 06:30 pm<br>Sat - Sun: <b>Closed</b><br>Live help: <b>Available | 24/7</b></div></div>
  <div class="abs f-col" style="left:871px;top:3963px"><h5>Contact Info</h5><div>General Enquiries: +00 1 555 0140<br>Customer Service: +00 1 555 0141<br>Investor Enquiries: +00 1 555 0142<br>+00 1 555 0140<br>hello@plombek-mail.example</div></div>
  <div class="abs social"><span></span><span></span><span></span><span></span></div>
  <div class="abs f-line"></div>
  <div class="abs center copy">© 2023 Plombek. All Rights Reserved.</div>
  <div class="abs code">EK07</div>
</footer>

</body>
</html>
```